nestliva - Ballon Design

I need a Ballon designed. Please use the psb file ballon_template.psb as template.

I would like to have a ballon designed similar to the file "example.png".
instead of the pellu tot logo please use my attached logo "nestliva logo.ai"

The text should be the same " IT'S A MOM" but the logo should be different.

I should look like more elegant. should be also white background. But for the design feel free.

thanks.

Please also add the webpage "www.nestliva.eu" on the ballon design.

```html
<!DOCTYPE html>
<html lang="en">
<head>
<meta charset="UTF-8">
<title>nestliva – It's a Mom balloon</title>
<link rel="stylesheet" href="https://fonts.googleapis.com/css2?family=Fredoka:wght@500;600;700&display=swap">
<style>
  :root {
    --bg: #f4f5f7;
    --balloon: #ffffff;
    --balloon-edge: #c9ccd2;
    --pink: #d0819f;
    --blue: #3e5fa0;
  }
  html, body {
    margin: 0;
    padding: 0;
    width: 1200px;
    height: 1200px;
    overflow: hidden;
    background: var(--bg);
  }
  .canvas {
    width: 1200px;
    height: 1200px;
    display: flex;
    align-items: center;
    justify-content: center;
  }
  .balloon {
    width: 1040px;
    height: 1040px;
    border-radius: 50%;
    background: var(--balloon);
    border: 3px solid var(--balloon-edge);
    box-sizing: border-box;
    display: flex;
    flex-direction: column;
    align-items: center;
    justify-content: center;
  }
  .headline {
    margin: 0;
    font-family: "Fredoka", sans-serif;
    font-weight: 700;
    color: var(--pink);
    text-align: center;
    white-space: nowrap;
  }
  .headline > .line {
    display: block;
    font-size: 245px;
    line-height: 200px;
    height: 200px;
  }
  .headline > .line-mom {
    font-size: 260px;
    letter-spacing: -4px;
  }
  .mom-o {
    position: relative;
    display: inline-block;
  }
  .daisy {
    position: absolute;
    left: 50%;
    top: 52%;
    width: 64px;
    height: 64px;
    margin: -32px 0 0 -32px;
    border-radius: 50%;
    background: var(--balloon);
  }
  .brand {
    margin-top: 44px;
    display: flex;
    flex-direction: column;
    align-items: center;
    font-family: "Fredoka", sans-serif;
    color: var(--blue);
  }
  .brand-name {
    font-size: 86px;
    font-weight: 600;
    line-height: 1;
    letter-spacing: 1px;
  }
  .brand-url {
    margin-top: 12px;
    font-size: 32px;
    font-weight: 600;
    line-height: 1;
    letter-spacing: 1px;
  }
</style>
</head>
<body>
  <main class="canvas">
    <section class="balloon">
      <h1 class="headline">
        <span class="line line-its">IT’S</span>
        <span class="line line-a">A</span>
        <span class="line line-mom">M<span class="mom-o">O<span class="daisy" role="img" aria-label="White daisy flower inside the letter O"></span></span>M</span>
      </h1>
      <div class="brand">
        <span class="brand-name">nestliva</span>
        <span class="brand-url">www.nestliva.eu</span>
      </div>
    </section>
  </main>
</body>
</html>
```